Business card for a business coach / management consultant

My logo has been done and now I need a business card. Deliverable needs to be a PDF to give to the printer. I want it single sided as I want the back side blank.
I prefer a white card with modern simple professional design.
Details are:
Tobias Wrenfield
B.Sc. (hons) FRTB CP MEGOL
14 Calloway Rd
Brindle Park WA 6029
Australia
mobile 041 23 584 17
email tobias@corporatepathlane.com.au
skype tobiaswrenfield8
Small to medium size business owners
Business

```html
<!DOCTYPE html>
<html lang="en">
<head>
<meta charset="utf-8">
<title>Tobias Wrenfield – Business Card</title>
<link rel="stylesheet" href="https://fonts.googleapis.com/css2?family=Open+Sans:wght@400;500&display=swap">
<style>
  :root {
    --brand-green: #3db54a;
    --card-white: #ffffff;
    --ink: #1f1f1f;
    --logo-ink: #222222;
  }
  * { box-sizing: border-box; margin: 0; padding: 0; }
  html, body {
    width: 1200px;
    height: 900px;
    overflow: hidden;
    background: var(--card-white);
  }
  .card {
    position: relative;
    width: 1200px;
    height: 900px;
    background: var(--card-white);
    font-family: "Open Sans", Arial, sans-serif;
    color: var(--ink);
  }
  .card__shapes {
    position: absolute;
    inset: 0;
  }
  .identity {
    position: absolute;
    left: 450px;
    top: 76px;
    width: 296px;
    text-align: center;
    color: var(--card-white);
  }
  .identity__name {
    font-size: 33px;
    font-weight: 400;
    line-height: 1.15;
    white-space: nowrap;
  }
  .identity__credentials {
    margin-top: 4px;
    font-size: 16px;
    font-weight: 400;
    white-space: nowrap;
  }
  .logo-slot {
    position: absolute;
    left: 450px;
    top: 392px;
    width: 296px;
    text-align: center;
    font-family: Arial, Helvetica, sans-serif;
    font-size: 22px;
    letter-spacing: 1px;
    color: var(--logo-ink);
  }
  .address {
    position: absolute;
    left: 400px;
    top: 626px;
    width: 396px;
    text-align: center;
    font-size: 22px;
    line-height: 30px;
    font-style: normal;
  }
  .contacts {
    position: absolute;
    left: 350px;
    top: 744px;
    width: 496px;
    list-style: none;
    text-align: center;
    font-size: 22px;
    line-height: 28px;
  }
  .contacts__item {
    display: flex;
    justify-content: center;
    align-items: center;
    gap: 8px;
  }
  .contacts__icon {
    width: 24px;
    height: 20px;
    flex: none;
  }
</style>
</head>
<body>
<main class="card">
  <svg class="card__shapes" width="1200" height="900" viewBox="0 0 1200 900" aria-hidden="true">
    <rect class="name-band" x="450" y="10" width="296" height="340" fill="var(--brand-green)"/>
    <circle class="logo-halo" cx="598" cy="410" r="162" fill="var(--card-white)"/>
    <circle class="logo-ring" cx="598" cy="410" r="146" fill="var(--card-white)" stroke="var(--brand-green)" stroke-width="4"/>
  </svg>

  <header class="identity">
    <h1 class="identity__name">Tobias Wrenfield</h1>
    <p class="identity__credentials">B.Sc. (hons) FRTB CP MEGOL</p>
  </header>

  <p class="logo-slot">LOGO HERE</p>

  <address class="address">
    14 Calloway Rd<br>
    Brindle Park WA 6029,<br>
    Australia
  </address>

  <ul class="contacts">
    <li class="contacts__item">
      <svg class="contacts__icon" viewBox="0 0 24 20" aria-label="Phone" role="img">
        <path d="M2 7c0-3 4-5 10-5s10 2 10 5v2h-5V7c-1-1-3-1.5-5-1.5S8 6 7 7v2H2z" fill="var(--brand-green)"/>
        <path d="M6 10l2-3h8l2 3v7H6z" fill="var(--brand-green)"/>
        <circle cx="12" cy="13" r="2.2" fill="var(--card-white)"/>
      </svg>
      <span>041 23 584 17</span>
    </li>
    <li class="contacts__item">
      <svg class="contacts__icon" viewBox="0 0 24 20" aria-label="Email" role="img">
        <rect x="1.5" y="3" width="21" height="14" fill="none" stroke="var(--brand-green)" stroke-width="1.8"/>
        <path d="M1.5 3l10.5 8 10.5-8M1.5 17l8-7M22.5 17l-8-7" fill="none" stroke="var(--brand-green)" stroke-width="1.6"/>
      </svg>
      <span>tobias@corporatepathlane.com.au</span>
    </li>
    <li class="contacts__item">
      <svg class="contacts__icon" viewBox="0 0 24 20" aria-label="Messaging" role="img">
        <circle cx="12" cy="10" r="7" fill="var(--brand-green)"/>
      </svg>
      <span>tobiaswrenfield8</span>
    </li>
  </ul>
</main>
</body>
</html>
```